Redesign of a Brochure based on an exsiting example for Web download and email marketing

Can you create a professional brochure based on the attached PDF. We need to keep the name, the logo and the content but everything else can be changed . The PDF will primarily be will be used for web download and email marking but it aslo be printed out for a poster design will be appropriate

Target Market(s)

Business to Business

Industry/Entity Type

Marketing

Font styles to use
Serif

Requirements
Must have
• Must have the existing logo ( in the attached document) and contain the same content

```html
<!DOCTYPE html>
<html lang="en">
<head>
<meta charset="utf-8">
<title>Veltrane – IT RUN Model 1 Brochure</title>
<link href="https://fonts.googleapis.com/css2?family=Raleway:wght@300;400;500;600;700&family=Cinzel:wght@400&display=swap" rel="stylesheet">
<style>
:root{
  --stage:#8a8a8a;
  --paper:#ffffff;
  --navy:#1c2f5e;
  --accent:#4f81c4;
  --accent-soft:#8fb2e0;
  --ink:#222a3a;
  --muted:#6d7280;
  --rule:#c9d3e6;
}
*{margin:0;padding:0;box-sizing:border-box}
html,body{width:1200px;height:1200px;overflow:hidden;background:var(--stage)}
body{font-family:"Raleway",sans-serif;color:var(--ink);position:relative}
.page{position:absolute;width:576px;height:432px;background:var(--paper);overflow:hidden}
.p1{left:19px;top:127px}.p2{left:608px;top:127px}
.p3{left:19px;top:585px}.p4{left:608px;top:585px}
.abs{position:absolute}
.brand{position:absolute;left:421px;top:0;width:132px;height:67px;background:var(--navy);color:#fff;display:flex;flex-direction:column;align-items:center;justify-content:center}
.brand-name{font-family:"Cinzel",serif;font-size:12px;letter-spacing:2.5px;display:flex;align-items:center;gap:6px}
.brand-name i{display:block;width:8px;height:8px;background:#fff}
.brand-tag{font-size:6.5px;font-weight:300;margin-top:4px;color:#cfd8ea;padding-left:14px}
.cover-band{position:absolute;left:421px;top:0;width:132px;height:432px;background:radial-gradient(circle at 30% 45%,#3b4f80 0,#2a3d6d 35%,var(--navy) 60%),var(--navy)}
.cover-meta{position:absolute;right:180px;top:205px;text-align:right}
.cover-meta dt{font-size:11.5px;color:var(--navy);font-weight:400;letter-spacing:.6px;margin-top:15px}
.cover-meta dt:first-child{margin-top:0}
.cover-meta dd{font-size:11.5px;color:var(--navy);font-weight:700;letter-spacing:.6px}
.tab{position:absolute;left:0;width:18px;background:var(--accent)}
.heading{position:absolute;left:27px;border-bottom:1px solid var(--accent-soft);color:var(--navy)}
.heading .kicker{font-size:12px;color:var(--accent);font-weight:400}
.heading h1{font-size:12.5px;font-weight:700;padding-bottom:3px}
.heading h2{font-size:9.5px;font-weight:400;line-height:1.1;padding-bottom:4px}
.body{font-size:6.5px;line-height:1.85;color:#4a4f5c;text-align:justify;font-weight:400}
.body p{margin-bottom:8px}
.body ul{list-style:none}
.body li::before{content:"• "}
.folio{position:absolute;left:27px;bottom:12px;font-size:6px;color:var(--muted)}
.footnote{position:absolute;right:30px;bottom:18px;font-size:4.5px;color:var(--muted);border-top:1px solid var(--rule);padding-top:3px;width:220px;text-align:right}
.tb{position:absolute;background:var(--accent);color:#fff;font-size:7.5px;display:flex;align-items:center;justify-content:center;border-radius:2px;box-shadow:0 1px 2px rgba(0,0,0,.2)}
.tb::before{content:"";position:absolute;left:0;right:0;top:-4px;border-top:1px solid var(--muted)}
.col{position:absolute;font-size:6px;line-height:11px;color:var(--muted);white-space:nowrap}
.col b{color:var(--navy);font-weight:700}
.col .i1{padding-left:8px}.col .i2{padding-left:16px}.col .i3{padding-left:24px}
.layer-line{position:absolute;width:1px;background:var(--accent-soft)}
.layer-line::before{content:"";position:absolute;left:-3px;top:-6px;width:7px;height:7px;border:1px solid var(--accent);border-radius:50%;background:#fff}
.layer-head{position:absolute;font-size:9px;line-height:1.15;color:var(--navy);font-weight:600}
.layer-head span{display:block;color:var(--accent);font-weight:400}
.vbar{position:absolute;width:20px;background:var(--accent);border-radius:3px 3px 0 0}
.vbar span{position:absolute;left:50%;bottom:8px;transform-origin:left bottom;transform:rotate(-90deg) translate(0,50%);color:#fff;font-weight:600;font-size:10px;white-space:nowrap;margin-left:-1px}
.pie-label{font-size:5.5px;fill:#9aa0ab;font-family:"Raleway",sans-serif}
</style>
</head>
<body>

<section class="page p1">
  <div class="cover-band" role="img" aria-label="Deep navy band with soft overlapping translucent circles"></div>
  <div class="brand" style="background:transparent">
    <div class="brand-name"><i></i>VELTRANE</div>
    <div class="brand-tag">IT Cost Transparency</div>
  </div>
  <dl class="cover-meta">
    <dt>Date Published:</dt><dd>05 June 2015</dd>
    <dt>Published Model Number:</dt><dd>100001</dd>
    <dt>Author:</dt><dd>Veltrane</dd>
    <dt>Contact:</dt><dd>j.harlow@bramwellpark.co.uk</dd>
    <dt>Related models:</dt><dd>IT Build Model 1 - 100002</dd>
  </dl>
</section>

<section class="page p2">
  <div class="brand"><div class="brand-name"><i></i>VELTRANE</div><div class="brand-tag">IT Cost Transparency</div></div>
  <div class="tab" style="top:30px;height:37px"></div>
  <div class="heading" style="top:35px;width:250px"><div class="kicker">Model Name:</div><h1>IT RUN Model 1</h1></div>
  <div class="body abs" style="left:27px;top:80px;width:250px">
    <p>IT Run Model 1 is a simple IT costing model suitable for any industry. It is designed to support a sophisticated level of cost transparency across common IT technologies, towers and services with a minimum of effort. As a starting point this model is mainly focused on the IT costs that “run” the business. However, it can be extended to cover a detailed view of IT investments that “change” the business as well. In addition, it can be used as a starting point to manage demand by extending support for specific business processes.</p>
    <p>This model is a concrete implementation of the Technology Business Management (TBM) standard framework.*</p>
    <p style="margin-bottom:2px">TBM has three main views:</p>
    <ul style="margin-bottom:8px"><li>Finance View,</li><li>IT View,</li><li>Business view.</li></ul>
    <p>This model implements these views through three simple layers; IT Cost centres, IT Technology Towers and Products &amp; Services.</p>
    <p>You can start by implementing just the IT Cost Centres to get some valuable insights before moving on to the IT Towers and Product/Services layers.</p>
  </div>
  <div class="abs" style="left:300px;top:115px;width:17px;height:38px;background:var(--accent)"></div>
  <div class="heading" style="left:326px;top:120px;width:222px"><h2>Tech Towers<br>(Run Build Manage)</h2></div>
  <svg class="abs" style="left:290px;top:180px" width="286" height="150" viewBox="0 0 286 150">
    <g transform="translate(128,65)">
      <circle r="48" fill="none" stroke="var(--accent)" stroke-width="1.5"/>
      <path d="M0 0L-22 -38.1A44 44 0 0 1 43.3 -7.6Z" fill="#fcc95a"/>
      <path d="M0 0L43.3 -7.6A44 44 0 0 1 39.9 18.6Z" fill="#a98bc9"/>
      <path d="M0 0L39.9 18.6A44 44 0 0 1 36 25.2Z" fill="#7fcf9a"/>
      <path d="M0 0L36 25.2A44 44 0 0 1 -38.1 22Z" fill="#86c9ee"/>
      <path d="M0 0L-38.1 22A44 44 0 0 1 -42.5 -11.4Z" fill="#ee6f73"/>
      <path d="M0 0L-42.5 -11.4A44 44 0 0 1 -22 -38.1Z" fill="#f8ef85"/>
      <g stroke="#9aa0ab" stroke-width=".6" fill="#fff">
        <line x1="-26" y1="-40" x2="-35" y2="-49"/><circle cx="-35" cy="-49" r="2.5" stroke="#e6b84a"/>
        <line x1="30" y1="-38" x2="40" y2="-52"/><circle cx="40" cy="-52" r="2.5" stroke="#e6b84a"/>
        <line x1="47" y1="8" x2="60" y2="8"/><circle cx="60" cy="8" r="2.5" stroke="#8f6fb6"/>
        <line x1="40" y1="28" x2="52" y2="33"/><circle cx="52" cy="33" r="2.5" stroke="#5bb67b"/>
        <line x1="-47" y1="8" x2="-52" y2="8"/><circle cx="-52" cy="8" r="2.5" stroke="#e05a5e"/>
        <line x1="-8" y1="47" x2="-12" y2="55"/><circle cx="-12" cy="55" r="2.5" stroke="#5aa5d8"/>
      </g>
    </g>
    <text class="pie-label" x="18" y="17">Datacentre &amp; Servers</text>
    <text class="pie-label" x="174" y="11">Apps Maintenance</text>
    <text class="pie-label" x="194" y="75">Helpdesk &amp; Ops Bridge</text>
    <text class="pie-label" x="187" y="100">Not Allocated</text>
    <text class="pie-label" x="9" y="75">End User Computing</text>
    <text class="pie-label" x="94" y="133">Networks &amp; Telecoms</text>
  </svg>
  <div class="folio">page 2</div>
  <div class="footnote">* For Technology Business Management (TBM) see costframework.org</div>
</section>

<section class="page p3">
  <div class="brand"><div class="brand-name"><i></i>VELTRANE</div><div class="brand-tag">IT Cost Transparency</div></div>
  <div class="tab" style="top:30px;height:37px"></div>
  <div class="heading" style="top:35px;width:250px"><h2>Technology Business Management<br>(TBM) Framework</h2></div>
  <div class="tb" style="left:27px;top:114px;width:250px;height:24px">Business Units</div>
  <div class="tb" style="left:27px;top:157px;width:107px;height:24px">Products</div>
  <div class="tb" style="left:170px;top:157px;width:107px;height:24px">Services</div>
  <div class="tb" style="left:27px;top:199px;width:250px;height:24px">Technology Towers</div>
  <div class="tb" style="left:27px;top:242px;width:250px;height:24px">Cost Pools: Standardised Costs</div>
  <div class="tb" style="left:27px;top:285px;width:250px;height:25px">Finance Layer: General Ledger Cost</div>
  <svg class="abs" style="left:0;top:0" width="300" height="300" viewBox="0 0 300 300" fill="none" stroke="#666" stroke-width="1">
    <path d="M81 151V141M77 145L81 141L85 145"/><path d="M224 151V141M220 145L224 141L228 145"/>
    <path d="M81 194V184M77 188L81 184L85 188"/><path d="M224 194V184M220 188L224 184L228 188"/>
    <path d="M152 237V227M148 231L152 227L156 231"/>
    <path d="M152 280V270"/>
  </svg>
  <div class="body abs" style="left:299px;top:110px;width:250px;line-height:1.8">
    <p style="margin-bottom:0">TBM provides a simple but clear way to describe IT costs and how they build into technology towers, services and applications. The next page details the model layers and categories. It splits costs over three broad categories:</p>
    <p style="margin-bottom:0">•Build,<br>•Manage<br>•Run.</p>
    <p style="margin-bottom:0">In TBM terminology “Run” is IT that supports the existing business, while “Build” is equivalent to change the business.</p>
    <p style="margin-bottom:0">The TBM model is shown in the diagram opposite. It does not, however, show the projects layer as this is part of the “change-the-business” IT spend and this model focuses mainly on “run-the-business” IT.</p>
    <p>The cost reference point of the model is the General Ledger, meaning there is always a clear reconciliation with corporate financial systems i.e. A single point of truth.</p>
  </div>
  <div class="folio">page 3</div>
  <div class="footnote">* For Technology Business Management (TBM) see costframework.org</div>
</section>

<section class="page p4">
  <div class="brand"><div class="brand-name"><i></i>VELTRANE</div><div class="brand-tag">IT Cost Transparency</div></div>
  <div class="tab" style="top:30px;height:37px"></div>
  <div class="heading" style="top:40px;width:250px"><h2>Model Layers &amp; Categories</h2></div>

  <div class="layer-line" style="left:48px;top:93px;height:295px"></div>
  <div class="layer-line" style="left:185px;top:93px;height:295px"></div>
  <div class="layer-line" style="left:425px;top:93px;height:295px"></div>

  <div class="vbar" style="left:24px;top:275px;height:104px"><span>IT Cost Centers</span></div>
  <div class="vbar" style="left:161px;top:219px;height:160px"><span>Tech Towers &amp; Sub Towers</span></div>
  <div class="vbar" style="left:401px;top:234px;height:145px"><span>Applications &amp; Services</span></div>

  <div class="layer-head" style="left:57px;top:99px">Layer 1<span>Run, Build &amp; Manage</span></div>
  <div class="layer-head" style="left:194px;top:99px">Layer 2<span>Run only</span></div>
  <div class="layer-head" style="left:434px;top:99px">Layer 3<span>Run only</span></div>

  <div class="col" style="left:57px;top:128px">
    <div><b>1. IT Staff</b></div><div>1.1 IT Staff Internal</div><div>1.2 IT Staff External</div>
    <div><b>2. Software</b></div><div>2.1 Depreciation</div><div>2.2 Lease</div><div>2.3 Expensed</div><div>2.4 Maintenance &amp; Support</div>
    <div><b>3. Hardware</b></div><div>3.1 Depreciation</div><div>3.2 Lease</div><div>3.3 Expensed</div><div>3.4 Maintenance &amp; Support</div>
    <div><b>4. Facilities &amp; Power</b></div><div>4.1 Depreciation</div><div>4.2 Rent/Lease</div><div>4.3 Expensed</div><div>4.4 Facilities Management</div><div>4.5 Electricity</div>
    <div><b>5. Third-Party</b></div><div>5.1 IT Consulting</div><div>5.2 Managed Services</div><div>5.3 Cloud Services</div><div>5.4 Other Services</div>
  </div>

  <div class="col" style="left:194px;top:128px">
    <div><b>1. Networks &amp; Telecoms</b></div><div>1.1 Networks</div><div class="i1">1.1.1 WAN</div><div class="i1">1.1.2 LAN</div>
    <div>1.2 Telecoms</div><div class="i1">1.2.1 Fixed Line</div><div class="i1">1.2.2 Mobile</div><div class="i1">1.2.3 Video Conferencing</div>
    <div><b>2. End User Computing</b></div><div>2.1 Desktop PC</div><div>2.2 Laptop</div><div>2.3 Tablet</div><div>2.4 Printers</div><div>2.5 EUC Support</div>
    <div><b>3. Datacentre and Servers</b></div><div>3.1 Datacentre</div><div class="i1">3.1.1 Buildings &amp; Rent</div><div class="i1">3.1.2 Electricity</div><div class="i1">3.1.3Datacentre Equipment</div><div class="i1">3.1.4 Datacentre Support</div>
    <div>3.2 Servers &amp; Storage</div><div class="i1">3.2.1 Mainframe</div><div class="i1">3.2.2 Midrange</div><div class="i1">3.2.3 X86</div>
  </div>

  <div class="col" style="left:302px;top:128px">
    <div class="i1">3.2.3.1 Processing</div><div class="i1">3.2.3.2 Storage</div><div class="i3">1 NAS</div><div class="i3">2 SAN</div><div class="i3">3 DAS</div><div class="i3">4 TAPE</div>
    <div>3.3 Co-Located Datacentres</div><div class="i1">3.3.2 Rack Unit Fees</div><div class="i1">3.3.1 Set-up Fees</div>
    <div><b>4. Applications</b></div><div>4.1 Applications Maintenance</div><div>4.2 Software Licensing</div><div>4.3 SaaS</div>
    <div><b>5. Cloud &amp; Hosting</b></div><div>5.1 Cloud Compute</div><div>5.2 Cloud Storage</div><div class="i2">1 NAS</div><div class="i2">2 SAN</div><div class="i2">3 Archive &amp; Backup</div><div>5.3 App &amp; Web Hosting</div><div>5.4 Cloud Other</div>
    <div><b>6. Service Operations</b></div><div>6.1 Helpdesk</div><div>6.2 Operations Bridge</div>
  </div>

  <div class="col" style="left:434px;top:128px">
    <div>1. IT Staff</div><div>1.1 IT Staff Internal</div><div>1.2 IT Staff External</div>
    <div><b>2. Software</b></div><div>2.1 Depreciation</div><div>2.2 Lease</div><div>2.3 Expensed</div><div>2.4 Maintenance &amp; Support</div>
    <div><b>3. Hardware</b></div><div>3.1 Depreciation</div><div>3.2 Lease</div><div>3.3 Expensed</div><div>3.4 Maintenance &amp; Support</div>
    <div><b>4. Facilities &amp; Power</b></div><div>4.1 Depreciation</div><div>4.2 Rent/Lease</div><div>4.3 Expensed</div><div>4.4 Facilities Management</div><div>4.5 Electricity</div>
    <div><b>5. Third-Party</b></div><div>5.1 IT Consulting</div><div>5.2 Managed Services</div><div>5.3 Cloud Services</div><div>5.4 Other Services</div>
  </div>
  <div class="folio">page 4</div>
</section>

</body>
</html>
```